Need Stunning, Visual Tree Identification Booklet

We are looking for a magazine/booklet style design for tree and plant identification. They need to be organized according to tree/plant type and contain a picture and tree/plant information. I would like to see 4 trees/plants per page. I will be including links for all the information needed but you will be responsible for gathering pictures as we have none to provide. This is not a booklet that will be sold or given out, it is solely to be used by our company internally for training and for presenting during sales meetings.

Target Market(s)

To be used by our sales staff when meeting with customers and selling trees and plants.

Industry/Entity Type

Landscape Gardening

Font styles to use
Serif

Requirements
Must have
• Attractive design that makes it easy to read and visual the trees and plants shown in the booklet. Design must be done in Adobe Illustrator or Adobe InDesign. Every tree/plant must have a picture, description, common name, Botanical name, Height, Width, Growth Rate, Function, Hardiness and Water Use. Would like to fit 4 trees/plants per page. Attached is a category outline.
Nice to have
• Clean, professional look. Using greens, whites and blacks

```html
<!DOCTYPE html>
<html lang="en">
<head>
<meta charset="utf-8">
<title>Tree &amp; Plant Identification – Booklet Covers</title>
<link href="https://fonts.googleapis.com/css2?family=Arvo:wght@700&family=Alfa+Slab+One&family=Cormorant+Garamond:wght@500;600&display=swap" rel="stylesheet">
<style>
  :root {
    --canvas-bg: #d9d9d9;
    --green: #2bb04a;
    --green-soft: #8fd49b;
    --white: #ffffff;
    --black: #0b0b0b;
    --title-green: #2a9f44;
  }
  * { box-sizing: border-box; margin: 0; padding: 0; }
  html, body {
    width: 1200px; height: 1200px; overflow: hidden;
    background: var(--canvas-bg);
  }
  .canvas {
    width: 1200px; height: 1200px;
    display: flex; justify-content: center; align-items: center; gap: 60px;
  }
  .cover {
    position: relative;
    width: 500px; height: 645px;
    background: radial-gradient(ellipse 62% 58% at 50% 50%, var(--white) 0%, #eaf7ec 35%, var(--green-soft) 75%, var(--green) 100%);
    overflow: hidden;
  }
  .cover__top-band {
    position: absolute; left: 0; top: 0; width: 100%; height: 41px;
    background: linear-gradient(180deg, var(--green) 0%, var(--green-soft) 60%, var(--white) 100%);
  }
  .cover__top-rule {
    position: absolute; left: 0; top: 45px; width: 100%; height: 17px;
    background: var(--black);
  }
  .cover__phone-band {
    position: absolute; left: 0; top: 570px; width: 100%; height: 41px;
    background: linear-gradient(90deg, var(--green) 0%, var(--green-soft) 15%, var(--white) 40%, var(--white) 60%, var(--green-soft) 85%, var(--green) 100%);
    display: flex; align-items: center; justify-content: center;
  }
  .cover__phone {
    font-family: "Arvo", serif; font-weight: 700; font-size: 27px;
    color: var(--black); letter-spacing: 0.04em;
  }
  .cover__web-rule {
    position: absolute; left: 0; top: 611px; width: 100%; height: 18px;
    background: var(--black);
    display: flex; align-items: center; justify-content: center;
  }
  .cover__web {
    font-family: "Cormorant Garamond", serif; font-weight: 600; font-size: 11px;
    color: var(--white); letter-spacing: 0.55em;
  }
  .cover__bottom-band {
    position: absolute; left: 0; top: 629px; width: 100%; height: 16px;
    background: linear-gradient(90deg, var(--green), var(--green-soft) 50%, var(--green));
  }
  .brand {
    position: absolute; left: 0; width: 100%;
    display: flex; flex-direction: column; align-items: center; gap: 10px;
  }
  .brand__mark {
    width: 96px; height: 96px; border-radius: 50%;
    border: 3px solid var(--black);
  }
  .brand__name {
    font-family: "Arvo", serif; font-weight: 700; font-size: 22px;
    color: var(--black); letter-spacing: 0.04em;
  }
  .cover--front .brand { top: 165px; }
  .cover--back .brand { top: 240px; }
  .title {
    position: absolute; left: 0; top: 378px; width: 100%; text-align: center;
  }
  .title__main {
    font-family: "Alfa Slab One", serif; font-size: 38px; line-height: 1;
    color: var(--title-green); letter-spacing: 0.01em;
  }
  .title__amp {
    font-family: "Cormorant Garamond", serif; font-weight: 500; font-size: 26px;
    color: var(--title-green);
  }
  .title__sub {
    margin-top: 6px;
    font-family: "Cormorant Garamond", serif; font-weight: 600; font-size: 17px;
    color: var(--black); letter-spacing: 0.55em; padding-left: 0.55em;
  }
</style>
</head>
<body>
  <main class="canvas">
    <section class="cover cover--front">
      <div class="cover__top-band"></div>
      <div class="cover__top-rule"></div>
      <div class="brand">
        <div class="brand__mark"></div>
        <div class="brand__name">OAKLINE CREW</div>
      </div>
      <div class="title">
        <div class="title__main">TREE <span class="title__amp">&amp;</span> PLANT</div>
        <div class="title__sub">IDENTIFICATION</div>
      </div>
      <div class="cover__phone-band"><span class="cover__phone">(000) 444-1234</span></div>
      <div class="cover__web-rule"><span class="cover__web">WWW.DOMAIN.COM</span></div>
      <div class="cover__bottom-band"></div>
    </section>

    <section class="cover cover--back">
      <div class="cover__top-band"></div>
      <div class="cover__top-rule"></div>
      <div class="brand">
        <div class="brand__mark"></div>
        <div class="brand__name">OAKLINE CREW</div>
      </div>
      <div class="cover__phone-band"><span class="cover__phone">(000) 444-1234</span></div>
      <div class="cover__web-rule"><span class="cover__web">WWW.DOMAIN.COM</span></div>
      <div class="cover__bottom-band"></div>
    </section>
  </main>
</body>
</html>
```